Album Cover Art for New Single

Independent singer-songwriter and pianist, seeking design work for a new single "Walk Along the Harbor". Christian & Gospel music format. See attached for master recording.

This single is personal for me, so I'm looking for an image that really captures the heart of the message. Redemption, forgiveness, prodigals returning home to a loving father.
Updates

Target Market(s)

Millenials

Colors

Designer to choose colors to be used in the design.

Requirements
Must have
• simple graphic, must include the following text:
• Walk Along the Harbor
• Dale Fennimore
Should not have
• Avoid "cheesy" look and feel.

```html
<!DOCTYPE html>
<html lang="en">
<head>
<meta charset="utf-8">
<title>Walk Along the Harbor — Dale Fennimore</title>
<link rel="stylesheet" href="https://fonts.googleapis.com/css2?family=Kaushan+Script&family=Montserrat:wght@800&display=swap">
<style>
  :root {
    --page: #ffffff;
    --sky-light: #e9c9a4;
    --sky-mid: #5e7a86;
    --sky-deep: #34475c;
    --sky-night: #27344d;
    --band: rgba(255, 255, 255, 0.10);
    --frame: #0b0b0e;
    --title: rgba(255, 255, 255, 0.9);
    --name: #ffffff;
    --name-shadow: #5a5f6c;
  }
  * { margin: 0; padding: 0; box-sizing: border-box; }
  html, body {
    width: 1200px;
    height: 1000px;
    overflow: hidden;
    background: var(--page);
  }
  .canvas {
    position: relative;
    width: 1200px;
    height: 1000px;
  }
  .cover {
    position: absolute;
    left: 131px;
    top: 41px;
    width: 920px;
    height: 920px;
    overflow: hidden;
  }
  .cover-photo {
    position: absolute;
    inset: 0;
    background:
      radial-gradient(ellipse 360px 300px at 40px 190px, rgba(245, 214, 170, 0.85), transparent 70%),
      radial-gradient(ellipse 300px 200px at 330px 120px, rgba(226, 184, 150, 0.45), transparent 75%),
      radial-gradient(ellipse 260px 420px at 720px 720px, rgba(30, 38, 60, 0.55), transparent 75%),
      linear-gradient(170deg, var(--sky-mid) 0%, var(--sky-deep) 45%, var(--sky-night) 100%);
  }
  .light-band {
    position: absolute;
    top: 0;
    height: 920px;
    background: var(--band);
  }
  .light-band--outer { left: 39px; width: 170px; }
  .light-band--inner { left: 0; width: 39px; background: rgba(255, 255, 255, 0.05); }
  .frames {
    position: absolute;
    left: 0;
    top: 0;
  }
  .title {
    position: absolute;
    font-family: "Kaushan Script", cursive;
    color: var(--title);
    font-weight: 400;
    white-space: nowrap;
    line-height: 1;
  }
  .title-line {
    position: absolute;
    font-size: 138px;
  }
  .title-line--first { left: 250px; top: 285px; }
  .title-line--second { left: 375px; top: 450px; }
  .artist {
    position: absolute;
    left: 413px;
    top: 890px;
    font-family: "Montserrat", sans-serif;
    font-weight: 800;
    font-size: 31px;
    letter-spacing: 20px;
    color: var(--name);
    text-shadow: -5px 3px 0 var(--name-shadow);
    white-space: nowrap;
    line-height: 1;
  }
</style>
</head>
<body>
<main class="canvas">
  <section class="cover">
    <div class="cover-photo" role="img" aria-label="Photograph of a stormy, cloud-filled sky with warm light breaking through at the upper left and a curly-haired child with a backpack seen from behind at the lower right"></div>
    <div class="light-band light-band--inner"></div>
    <div class="light-band light-band--outer"></div>
  </section>

  <svg class="frames" width="1200" height="1000" viewBox="0 0 1200 1000" aria-hidden="true">
    <g fill="none" stroke="var(--frame)" stroke-width="2">
      <polyline class="frame-outer" points="853,840 211,840 211,122 904,122 904,420"/>
      <polyline class="frame-inner" points="305,163 946,163 946,882 255,882 255,585"/>
    </g>
  </svg>

  <h1 class="title">
    <span class="title-line title-line--first">Walk Along</span>
    <span class="title-line title-line--second">the Harbor</span>
  </h1>

  <p class="artist">DALE FENNIMORE</p>
</main>
</body>
</html>
```